E-Book-Cover für meinen Roman Was der Nebel trägt
Sehr angenehmer Kontakt, das Beschriebene wurde auf Anhieb in die Richtung umgesetzt, die ich angestrebt habe. Änderungswünsche wurden prompt und unermüdlich umgesetzt, bis das Endergebnis stand. Sehr zu empfehlen!
Zielgruppe
Ich veröffentliche in Eigenregie meinen Roman namens 'Was der Nebel trägt' im Rahmen des Self-Publishing Angebots von Lesowa.de
Bei meinem Werk handelt es sich um Belletristik: eine Geschichte aus dem Leben, die traurige und lustige Elemente zu gleichen Teilen eint. Behandelt wird der Lebensabschnitt eines Jugendlichen, der zu früh Erfahrung mit dem Tod macht, als seine Mutter schwer erkrankt. Gleichzeitig gilt es, den (humorvoll verpackten) Alltag zu meistern, in dem er wieder und wieder auf Ablehnung und Distanz angesichts seiner ungewöhnlichen und misslichen Lage stößt. Es gelingt ihm nicht mehr, Teil seiner gleichaltrigen Mitstreiter zu werden.
Gleichzeitig gibt es einen zweiten Handlungsstrang, in dem eine ebenfalls Jugendliche ähnliche Erfahrungen macht, auch wenn die Umstände andere sind, ebenso wie die Reaktion darauf. Während der männliche Protagonist wiederholt von seinem Umkreis enttäuscht wird, stellt er sich am Ende der Prüfung, der er nicht entkommen kann. Sein weibliches Pendant hingegen tritt eine überstürzte Flucht mit ungewissem Ausgang an. Beide Stränge sind lose miteinander verwoben, und als Leser stellt man sich zusehends die Frage, ob und wann diese verbunden werden. Eine Auflösung erfolgt am Schluss.
Nach einigen Testlesern stellte sich heraus, dass jene am meisten begeistert waren, die selbst ähnliche Erfahrungen gemacht haben, wie die fiktiven Personen. Grundsätzlich lässt sich aber sagen, dass der Schreibstil, die beschriebenen Medien und Situationen eher auf (junge) Erwachsene zugeschnitten sind. Dennoch handelt es sich nicht um ein klassisches Jugendbuch, oft werden Dinge beschrieben, die für Minderjährige nicht geeignet sind. Als (Haupt)zielgruppe würde ich grob den Rahmen 20-40 Jahre vorgeben, wobei die Leser eher noch älter als jünger sein dürfen.
Aufgabenstellung
Zunächst technisch: (Angaben lt. Lesowa)
JPEG oder TIFF-Datei
mindestens 1000 Pixel an der längsten Seite
Idealverhältnis von Bildhöhe- und breite: 1,6 (Beispiel: 1000 x 1600)
bei weißen Covern sollte ein 2-3 Pixel breiter, grauer Rand hinzugefügt werden, damit sich das Cover von der Website selbst abhebt
Weiterhin zu beachten:
-Hauptsächlich wird es auf eBook Readern gelesen, die nur in Graustufen darstellen. Das Cover sollte also in jedem Fall auch in Schwarz-Weiß nichts von seiner Wirkung einbüßen!
Selbiges gilt für eine Miniaturansicht!
Autor: Matthias Krollner
Titel: Was der Nebel trägt
Zusatz: Roman
Nun zu den wichtigsten Vorgaben:
-Selbstverständlich soll das Cover Aufmerksamkeit erzeugen und neugierig machen.
-Das Thema "anders sein" / "im Abseits stehen" / "hin- und hergetrieben werden" muss auf jeden Fall rübergebracht werden, da dies auch das Kernthema des Buches ist.
-Bei der Schriftart gibt es keine bestimmte Vorgabe, nur bitte nichts in Kapitälchen oder Großbuchstaben. (z.B. WAS DER NEBEL TRÄGT)
-Es soll auf keinen Fall übertrieben ernst oder möchtegern-schnulzig rüberkommen. (Bilder vom Strand, untergehender Sonne und weitere Klischees.)
-Vielmehr darf man dem Cover bereits ansehen, dass es ein ernstes Thema auch mit Humor nehmen kann. z.B. durch Stilisierung, einfache Farben anstatt aufwändiger Realaufnahmen und Schatten, evtl. auch in Richtung Comic, aber nicht zu albern.
-Die Platzierung von Autor und Titel darf klassisch sein, gerne aber auch ungewöhnlich überraschend.
Ich habe diesem Inserat einige Entwürfe meinerseits beigefügt, wie ich das o.g. Thema stilisieren würde, z.B.:
der Querschnitt eines einfahrenden Zuges (Hauptverkehrsmittel im Buch), bei dem in allen Fenstern Licht brennt, mit Ausnahme von einem. (Hier dürfen gerne auch die Profile von Menschen hinzug..

```html
<!DOCTYPE html>
<html lang="de">
<head>
<meta charset="utf-8">
<title>Was der Nebel trägt – Matthias Krollner</title>
<link rel="stylesheet" href="https://fonts.googleapis.com/css2?family=Fira+Sans+Condensed:wght@700&family=Fira+Sans:wght@500&display=swap">
<style>
  :root {
    --page: #ffffff;
    --frame: #d9d9d9;
    --shadow: rgba(0, 0, 0, 0.12);
    --sky-red: #dd584b;
    --sky-soft: #e9968a;
    --field-rose: #eeb5c1;
    --field-pink: #d4486f;
    --title-pink: #d4486f;
    --title-red: #dd584b;
    --ink: #111111;
  }
  * { margin: 0; padding: 0; box-sizing: border-box; }
  html, body {
    width: 872px;
    height: 1200px;
    overflow: hidden;
    background: var(--page);
  }
  .cover {
    position: absolute;
    left: 123px;
    top: 103px;
    width: 617px;
    height: 990px;
    background: var(--page);
    border: 7px solid var(--frame);
    box-shadow: 2px 3px 4px var(--shadow);
    overflow: hidden;
  }
  .cover-art {
    position: absolute;
    left: 0;
    top: 0;
    width: 100%;
    height: 593px;
    display: block;
  }
  .title {
    font-family: "Fira Sans Condensed", "Fira Sans", sans-serif;
    font-weight: 700;
    line-height: 1;
    letter-spacing: -0.5px;
  }
  .title-line {
    position: absolute;
    left: 0;
    width: 100%;
    display: flex;
    justify-content: center;
    align-items: baseline;
    gap: 8px;
    white-space: nowrap;
  }
  .title-line--first { top: 547px; }
  .title-line--middle { top: 602px; }
  .title-line--last { top: 696px; }
  .title-word {
    font-size: 70px;
    color: var(--title-pink);
  }
  .title-word--key {
    font-size: 98px;
    color: var(--title-red);
  }
  .genre {
    position: absolute;
    left: 0;
    width: 100%;
    top: 776px;
    text-align: center;
    font-family: "Fira Sans", sans-serif;
    font-weight: 500;
    font-size: 22px;
    line-height: 1;
    letter-spacing: 0.5px;
    color: var(--title-red);
  }
  .author {
    position: absolute;
    left: 0;
    width: 100%;
    top: 842px;
    text-align: center;
    font-family: "Fira Sans", sans-serif;
    font-weight: 500;
    font-size: 38px;
    line-height: 1;
    color: var(--ink);
  }
</style>
</head>
<body>
  <main class="cover">
    <svg class="cover-art" viewBox="0 0 600 592" preserveAspectRatio="none" role="img"
         aria-label="Illustration: Bahngleise laufen zum Horizont, Oberleitungen darüber, eine kleine Gestalt geht allein auf den Schienen, roter Himmel über rosafarbenen Feldern">
      <defs>
        <linearGradient id="scene-tones" x1="0" y1="0" x2="0" y2="1">
          <stop offset="0" stop-color="#ffffff"/>
          <stop offset="0.16" stop-color="#ffffff"/>
          <stop offset="0.22" stop-color="var(--sky-red)"/>
          <stop offset="0.45" stop-color="var(--sky-red)"/>
          <stop offset="0.52" stop-color="var(--sky-soft)"/>
          <stop offset="0.56" stop-color="var(--field-rose)"/>
          <stop offset="0.64" stop-color="var(--field-pink)"/>
          <stop offset="0.74" stop-color="#e9a6b6"/>
          <stop offset="1" stop-color="#ffffff"/>
        </linearGradient>
      </defs>
      <rect x="0" y="0" width="600" height="592" fill="url(#scene-tones)"/>
    </svg>

    <h1 class="title" aria-label="Was der Nebel trägt">
      <span class="title-line title-line--first">
        <span class="title-word">Was</span>
      </span>
      <span class="title-line title-line--middle">
        <span class="title-word">der</span>
        <span class="title-word title-word--key">Nebel</span>
      </span>
      <span class="title-line title-line--last">
        <span class="title-word">trägt</span>
      </span>
    </h1>
    <p class="genre">Roman</p>
    <p class="author">Matthias Krollner</p>
  </main>
</body>
</html>
```